Insurance company needs a business card design

We need a business card design for a Massachusetts-based insurance company Veloria Insurance, LLC. We provide auto insurance to Hispanic (Spanish- or Portuguese-speaking) immigrants in the United States. We will give these business cards to auto dealers where such customers typically go to purchase vehicles. We will provide a solution to the dealers to provide easy insurance to the customers buying cars at their dealerships. Veloria is the Spanish word for protection.
Contact Information for Business Card
Name, Designation, Company Name, Address, Phone Number, Email, Website
Look and feel
Each slider illustrates characteristics of the customer's brand and the style your logo design should communicate.

```html
<!DOCTYPE html>
<html lang="en">
<head>
<meta charset="utf-8">
<title>Veloria Insurance business card</title>
<link rel="stylesheet" href="https://fonts.googleapis.com/css2?family=Montserrat:wght@400;600;700&display=swap">
<style>
  :root {
    --backdrop: #3a3a3a;
    --card: #161616;
    --card-back: #111111;
    --pattern-light: #1e1e1e;
    --orange: #f2891f;
    --blue: #1d4f86;
    --text: #ececec;
  }
  * { box-sizing: border-box; margin: 0; padding: 0; }
  html, body {
    width: 1200px; height: 801px; overflow: hidden;
    background: var(--backdrop);
    font-family: "Montserrat", sans-serif;
  }
  .stage {
    width: 1200px; height: 801px;
    display: flex; align-items: center; justify-content: center; gap: 48px;
  }
  .card {
    position: relative;
    width: 532px; height: 304px;
    background: var(--card);
    border-bottom: 3px solid var(--orange);
    border-left: 2px solid var(--orange);
    box-shadow: 0 14px 30px rgba(0,0,0,.35);
    overflow: hidden;
  }
  .brand {
    position: absolute; top: 50px; right: 46px;
    display: flex; align-items: center; gap: 10px;
    color: var(--blue); font-weight: 700; font-size: 22px;
    letter-spacing: 1px; text-transform: uppercase;
  }
  .brand-mark {
    width: 14px; height: 14px; background: var(--orange);
  }
  .divider {
    position: absolute; left: 40px; right: 40px; top: 170px;
    height: 1px; background: var(--blue);
  }
  .person { position: absolute; left: 40px; top: 122px; }
  .person-name {
    color: var(--orange); font-weight: 700; font-size: 19px;
    text-transform: uppercase; letter-spacing: .5px;
  }
  .person-title { color: var(--text); font-size: 12px; margin-top: 2px; }
  .contacts {
    position: absolute; left: 40px; top: 190px;
    list-style: none; color: var(--text); font-size: 12.5px;
  }
  .contacts li { display: flex; align-items: center; gap: 8px; height: 21px; }
  .contacts svg { width: 11px; height: 11px; fill: var(--orange); flex: none; }
  .address {
    position: absolute; right: 40px; top: 190px;
    color: var(--text); font-size: 12.5px; line-height: 21px; text-align: right;
  }
  .card-back { background: var(--card-back); }
  .pattern {
    position: absolute; inset: 0;
    background: linear-gradient(135deg, var(--pattern-light), var(--card-back) 60%, var(--pattern-light));
  }
  .back-brand {
    position: absolute; right: 70px; top: 120px;
    display: flex; align-items: center; gap: 8px;
    color: var(--blue); font-weight: 700; font-size: 16px;
    letter-spacing: 1px; text-transform: uppercase;
  }
</style>
</head>
<body>
<main class="stage">
  <section class="card card-front" aria-label="Card front">
    <div class="brand"><span class="brand-mark"></span>Veloria Insurance</div>
    <div class="person">
      <p class="person-name">Daniel Orvento</p>
      <p class="person-title">President</p>
    </div>
    <div class="divider"></div>
    <ul class="contacts">
      <li><svg viewBox="0 0 24 24"><path d="M6.6 10.8a15.1 15.1 0 0 0 6.6 6.6l2.2-2.2a1 1 0 0 1 1-.25 11.4 11.4 0 0 0 3.6.57 1 1 0 0 1 1 1V20a1 1 0 0 1-1 1A17 17 0 0 1 3 4a1 1 0 0 1 1-1h3.5a1 1 0 0 1 1 1c0 1.25.2 2.45.57 3.57a1 1 0 0 1-.25 1z"/></svg>555-240-6180</li>
      <li><svg viewBox="0 0 24 24"><path d="M2 5h20v14H2zm2 2v.5l8 5 8-5V7z"/></svg>info@veloriainsurance.com</li>
      <li><svg viewBox="0 0 24 24"><circle cx="12" cy="12" r="10"/></svg>www.veloriainsurance.com</li>
    </ul>
    <address class="address" style="font-style:normal">2180 Harbor Crest Way<br>Bayfield MA 02190</address>
  </section>
  <section class="card card-back" aria-label="Card back">
    <div class="pattern" role="img" aria-label="Repeating tone-on-tone brand emblem pattern in spot gloss on black"></div>
    <div class="back-brand"><span class="brand-mark" style="width:12px;height:12px;background:var(--orange)"></span>Veloria</div>
  </section>
</main>
</body>
</html>
```